PowerPoint Design for KELPO Polls

KELPO Polls stands for 'Kindred Estimates Linking Population Outlooks Polls'. It is a collaborative research effort to format and combine multiple sources of public opinion data from around the world into merged datasets. We need a Microsoft PowerPoint design for our conference/workshop presentations and instructional videos used as part of our research efforts and crowdsourced development. The design should match the website design and logo, which are attached to this contest (these are the files from previous successful design contests).

Slides will contain a lot of data visualizations, tables with statistical output (lots of numbers), and figures. Bullet points will be used frequently on slides and larg blocks of text should be avided. Margins should be narrow to maximize space used and the size of fonts must be large enough (24-32+) to be visible at the back of classrooms and conference rooms.

I was away at a conference and am now busy with teaching preparation, so I need a few extra days to give adequate feedback.

Target Market(s)

academia, government, non-profits, postgraduates, researchers

Font styles to use
Sans Serif

Colors

Designer to choose colors to be used in the design.

Requirements
Must have
• designs for common slide layouts
Nice to have
• thematic link with website design and logo

```html
<!DOCTYPE html>
<html lang="en">
<head>
<meta charset="utf-8">
<title>KELPO Polls – Slide Template Overview</title>
<link href="https://fonts.googleapis.com/css2?family=Open+Sans:wght@400;600;700&display=swap" rel="stylesheet">
<style>
:root{
  --blue:#1a87c9;
  --blue-dark:#136ea6;
  --blue-soft:#7fc0e6;
  --ink:#2b2b2b;
  --grey:#6a6a6a;
  --paper:#ffffff;
  --photo-a:#8a8f96;
  --photo-b:#c9cdd2;
}
*{box-sizing:border-box;margin:0;padding:0}
html,body{width:1200px;height:1200px;overflow:hidden;background:var(--paper);font-family:"Open Sans",Arial,sans-serif;color:var(--ink)}
.canvas{width:1200px;height:1200px;padding-top:3px}
.section-title{height:34px;line-height:34px;text-align:center;font-size:17px;font-weight:400;color:#333}
.deck{display:grid;grid-template-columns:repeat(8,150px);grid-auto-rows:114px}
.slide{position:relative;overflow:hidden;padding:8px 9px;font-size:5.2px;line-height:1.35}
.slide.w{background:var(--paper);color:var(--ink)}
.slide.b{background:var(--blue);color:#fff}
.slide::before,.slide::after{content:"";position:absolute;width:12px;height:12px;border:2px solid var(--blue)}
.slide::before{top:4px;right:4px;border-left:0;border-bottom:0}
.slide::after{bottom:4px;left:4px;border-right:0;border-top:0}
.slide.b::before,.slide.b::after{border-color:#fff}
.slide.cover::before,.slide.cover::after{display:none}
.t{font-size:7.4px;font-weight:700;margin-bottom:3px;text-align:center}
.slide.w .t{color:var(--blue-dark)}
.t.left{text-align:left;color:var(--ink)!important}
.sub{font-size:4.6px;text-align:center;opacity:.85;margin-bottom:4px}
.list{list-style:none}
.list li{display:flex;gap:3px;margin-bottom:3px;align-items:flex-start}
.num{flex:0 0 7px;height:7px;border:1px solid currentColor;font-size:4.5px;line-height:5px;text-align:center;font-weight:700}
.slide.w .num{color:var(--blue)}
.ico{flex:0 0 8px;height:8px;border:1px solid currentColor;border-radius:50%}
.slide.w .ico{color:#555}
.dots li::before{content:"•";margin-right:2px}
.ph{background:linear-gradient(135deg,var(--photo-a),var(--photo-b))}
.cover .ph{position:absolute;left:0;right:0;top:0;height:56%}
.brand{position:absolute;top:4px;right:8px;display:flex;gap:3px;align-items:center;font-size:5.4px;font-weight:600;color:var(--blue);z-index:2}
.brand i{width:5px;height:5px;background:var(--blue);display:block}
.cover .band{position:absolute;left:0;right:0;bottom:0;height:44%;background:var(--blue);color:#fff;text-align:center;font-weight:700;font-size:7.4px;display:flex;flex-direction:column;justify-content:center;padding:0 6px}
.cover .band small{font-weight:400;font-size:4.2px;margin-top:3px}
.part{display:flex;flex-direction:column;align-items:center;text-align:center}
.part .lbl{font-size:6.2px;letter-spacing:.5px;font-weight:700}
.part .ph{width:100px;height:54px;margin:4px 0;border:2px solid #fff}
table{border-collapse:collapse;width:100%;font-size:4.3px}
td,th{padding:0 2px;text-align:right;border-bottom:.5px solid rgba(0,0,0,.15);white-space:nowrap}
td:first-child,th:first-child{text-align:left}
.slide.b td,.slide.b th{border-color:rgba(255,255,255,.35)}
.tight td,.tight th{font-size:3.8px;line-height:1.25}
.two{display:flex;gap:5px}
.two>*{flex:1}
svg{display:block}
.box{border:1px solid var(--blue);padding:3px;text-align:center;font-size:4.6px}
.slide.b .box{border-color:#fff}
.bluebox{background:var(--blue);color:#fff;padding:3px;font-size:4.6px;text-align:center}
.empty{background:var(--paper)}
</style>
</head>
<body>
<div class="canvas">

<h2 class="section-title">CPSC 2017 Presentation Preview</h2>
<div class="deck">
  <div class="slide b cover"><div class="brand"><i></i>KELPO Polls</div><div class="ph" role="img" aria-label="Photo of a dense city crowd"></div><div class="band">Demographic Divides and Satisfaction with Democracy</div></div>
  <div class="slide w"><div class="t left">Introduction</div><ol class="list"><li><span class="num">1</span>Motivation of this study is to explain divisions in contemporary societies</li><li><span class="num">2</span>Relevant to understanding recent votes and similar electoral upsets</li><li><span class="num">3</span>Opinions of educational and income groups diverge with socioeconomic development</li><li><span class="num">4</span>Part of a larger comparative public opinion research project</li></ol></div>
  <div class="slide b"><div class="t">Public Opinion vs Expert Assessments</div><ol class="list"><li><span class="ico"></span>Create indices to represent particular demographic groups</li><li><span class="ico"></span>Compare these indices with expert indices measuring democratic quality</li><li><span class="ico"></span>Aim to determine if experts match opinions of some groups more than others</li><li><span class="ico"></span>Pairwise correlations between these indices as a simple test</li></ol></div>
  <div class="slide w"><div class="t">Comparative Public Opinion</div><div class="sub">Focus today: Satisfaction with Democracy</div><div class="two"><table class="tight" style="flex:1.4"><tr><th>Source</th><th>Resp.</th><th>Years</th></tr><tr><td>Barometer A</td><td>411,280</td><td>318</td></tr><tr><td>Barometer B</td><td>520,112</td><td>402</td></tr><tr><td>Barometer C</td><td>212,045</td><td>190</td></tr><tr><td>Barometer D</td><td>158,903</td><td>141</td></tr><tr><td>Social Survey</td><td>377,620</td><td>298</td></tr><tr><td>Values Study</td><td>296,018</td><td>254</td></tr></table><div class="ph" role="img" aria-label="Portrait photo of a smiling man" style="height:44px"></div></div><div style="margin-top:4px;border:1px solid var(--blue);padding:1px 3px;display:flex;justify-content:space-between;font-size:4.4px"><span>Satisfaction with Democracy</span><span>3,236,956 &nbsp; 2,619</span></div></div>
  <div class="slide b"><div class="t">Surveys Per Country</div><div class="sub">Study includes 150 countries from 1973 to 2015</div><div class="ph" role="img" aria-label="World map shaded by survey count" style="height:62px;background:linear-gradient(135deg,#5ea9d8,#a9d3ee)"></div></div>
  <div class="slide w"><div class="t">Typical Survey Question</div><div class="sub" style="color:var(--blue)">Four point response scale the most common</div><div class="two"><svg viewBox="0 0 60 60" width="58" height="58"><circle cx="30" cy="30" r="20" fill="none" stroke="#dce9f3" stroke-width="9"/><circle cx="30" cy="30" r="20" fill="none" stroke="var(--blue)" stroke-width="9" stroke-dasharray="98 126" transform="rotate(-90 30 30)"/><text x="30" y="32.5" font-size="7" font-weight="700" fill="#333" text-anchor="middle">78%</text></svg><div><p style="font-style:italic;margin-bottom:3px">On the whole, how satisfied are you with the way democracy works in your country?</p><div class="bluebox" style="margin-bottom:1px">Not at all satisfied</div><div class="bluebox" style="margin-bottom:1px">Not at very satisfied</div><div class="bluebox" style="margin-bottom:1px">Fairly satisfied</div><div class="bluebox">Very satisfied</div></div></div></div>
  <div class="slide b"><div class="t">Dependent Variable</div><div class="sub">Satisfaction with Democracy</div><div class="two"><div class="box">Values of different survey response scales converted to range from 0 to 100</div><div class="box">Values then averaged within each country-survey to produce scores</div></div><svg viewBox="0 0 120 40" width="128" height="42" style="margin-top:3px"><g fill="#fff"><rect x="30" y="34" width="3" height="4"/><rect x="34" y="30" width="3" height="8"/><rect x="38" y="26" width="3" height="12"/><rect x="42" y="20" width="3" height="18"/><rect x="46" y="14" width="3" height="24"/><rect x="50" y="8" width="3" height="30"/><rect x="54" y="4" width="3" height="34"/><rect x="58" y="2" width="3" height="36"/><rect x="62" y="5" width="3" height="33"/><rect x="66" y="10" width="3" height="28"/><rect x="70" y="16" width="3" height="22"/><rect x="74" y="22" width="3" height="16"/><rect x="78" y="28" width="3" height="10"/><rect x="82" y="32" width="3" height="6"/></g><line x1="10" y1="38" x2="110" y2="38" stroke="#fff" stroke-width=".5"/></svg></div>
  <div class="slide w"><div class="t left" style="color:var(--blue-dark)!important">Independent Variables</div><div class="sub" style="text-align:left;color:var(--blue)">Demographic groups common across surveys</div><div class="two"><ul class="list"><li><span class="ico"></span>Education: primary school or less versus at least some tertiary</li><li><span class="ico"></span>Income: lowest 25% versus highest 25% within each survey</li></ul><ul class="list"><li><span class="ico"></span>Age: people under 30 versus those over 50</li><li><span class="ico"></span>Gender: male versus female</li></ul></div></div>

  <div class="slide b"><div class="t">Demographic Divides</div><div class="sub">Groups diverge with rising development</div><ul class="list dots"><li>Horizontal: HDI scores</li><li>Vertical: Satisfaction with Democracy</li><li>Median lines for different groups</li></ul><div class="two"><svg viewBox="0 0 60 30" height="34"><rect width="60" height="30" fill="#fff"/><polyline points="4,20 20,17 36,14 56,9" fill="none" stroke="var(--blue)"/><polyline points="4,18 20,18 36,19 56,20" fill="none" stroke="#9bc9e8"/></svg><svg viewBox="0 0 60 30" height="34"><rect width="60" height="30" fill="#fff"/><polyline points="4,22 20,19 36,15 56,10" fill="none" stroke="var(--blue)"/><polyline points="4,19 20,18 36,18 56,17" fill="none" stroke="#9bc9e8"/></svg></div></div>
  <div class="slide w"><div class="t left" style="color:var(--blue-dark)!important">Demographic Divides</div><div class="sub" style="text-align:left;color:var(--blue)">Interactions with HDI scores</div><table class="tight" style="background:var(--blue);color:#fff"><tr><th></th><th>Odds</th><th>S.E.</th><th>Sig.</th></tr><tr><td>Primary Education</td><td>1.19</td><td>(0.05)</td><td>0.000</td></tr><tr><td>Primary Ed. x HDI</td><td>0.91</td><td>(0.06)</td><td>0.170</td></tr><tr><td>Tertiary Education</td><td>0.82</td><td>(0.04)</td><td>0.000</td></tr><tr><td>Tertiary Ed. x HDI</td><td>1.48</td><td>(0.11)</td><td>0.000</td></tr><tr><td>Lower Income</td><td>1.03</td><td>(0.04)</td><td>0.435</td></tr><tr><td>Lower Inc. x HDI</td><td>0.80</td><td>(0.05)</td><td>0.000</td></tr><tr><td>Higher Income</td><td>0.74</td><td>(0.04)</td><td>0.000</td></tr><tr><td>Higher Inc. x HDI</td><td>1.69</td><td>(0.13)</td><td>0.000</td></tr><tr><td>Age Under 30</td><td>1.04</td><td>(0.01)</td><td>0.002</td></tr><tr><td>Female Gender</td><td>0.95</td><td>(0.01)</td><td>0.000</td></tr></table></div>
  <div class="slide b"><div class="t">Control Variables</div><div class="two"><ul class="list" style="text-align:right"><li>Socioeconomic Development (HDI)</li><li>Income Inequality (Gini)</li><li>Institutionalised Democracy (Regime)</li><li>Corruption (CIX)</li><li>GDP Growth (Annual %)</li></ul><div class="ph" role="img" aria-label="Photo of a busy street market" style="height:80px"></div></div></div>
  <div class="slide w"><div class="t">Demographic Group Indices</div><div class="sub" style="color:var(--blue)">Satisfaction with democracy for different groups</div><ul class="list"><li><span class="ico"></span>Main index aggregates all respondents in each country-survey observation</li><li><span class="ico"></span>Educational indices measure only the opinions of primary or tertiary educated</li><li><span class="ico"></span>Income indices measure only the opinions of lower or higher income groups</li><li><span class="ico"></span>These indices are then compared with expert indices of democratic quality</li></ul></div>
  <div class="slide b"><div class="t">Democratic Quality Indices</div><div class="sub">Created by experts, institutions, and researchers</div><ol class="list"><li><span class="num">1</span>Civic Barometer (CB): Democratic Quality Index</li><li><span class="num">2</span>Civic Ledger Unit (CLU): Democracy Index</li><li><span class="num">3</span>Liberty Watch (LW): Global Liberty Score</li><li><span class="num">4</span>Regime Index (RI): Institutional Democracy</li><li><span class="num">5</span>Democracy Dimensions (DD): Egalitarian Democracy</li></ol></div>
  <div class="slide w"><div class="t">Comparisons with Expert Indices</div><div class="sub" style="color:var(--blue)">Pairwise correlations with public opinion indices</div><table class="tight" style="background:var(--blue);color:#fff"><tr><th></th><th>Main</th><th>Prim.</th><th>Tert.</th><th>Low</th><th>High</th></tr><tr><td>CB: Quality</td><td>0.49</td><td>0.37</td><td>0.54</td><td>0.40</td><td>0.46</td></tr><tr><td>CLU: Democracy</td><td>0.26</td><td>0.15</td><td>0.39</td><td>0.19</td><td>0.34</td></tr><tr><td>RI: Institutional</td><td>0.04</td><td>-0.02</td><td>0.14</td><td>0.03</td><td>0.12</td></tr><tr><td>LW: Liberty</td><td>0.17</td><td>0.01</td><td>0.76</td><td>0.09</td><td>0.76</td></tr><tr><td>DD: Egalitarian</td><td>0.19</td><td>0.09</td><td>0.21</td><td>0.15</td><td>0.27</td></tr></table><div class="sub" style="margin-top:2px">*** p &lt; 0.001 ** p &lt; 0.01 * p &lt; 0.05</div></div>
  <div class="slide b"><div class="t">Findings Summary</div><div class="sub">Results suggest general tendencies, exceptions possible</div><div style="display:flex;gap:4px;text-align:center"><div><span class="ico" style="display:block;margin:0 auto 2px;width:14px;height:14px"></span>Tertiary educated less satisfied in countries with lower HDI, more satisfied as HDI increases</div><div><span class="ico" style="display:block;margin:0 auto 2px;width:14px;height:14px"></span>Similar relationship for income groups, but not as strong</div><div><span class="ico" style="display:block;margin:0 auto 2px;width:14px;height:14px"></span>Democratic quality indices correlate more with tertiary educated and higher income groups</div></div></div>
  <div class="slide w"><div class="t left" style="color:var(--blue-dark)!important">References (1)</div><ul class="list" style="font-size:3.8px;line-height:1.5"><li>Author, A. (2014). Public opinion and regime support in new democracies. Journal of Politics 76(2).</li><li>Author, B. (2016). Measuring democratic quality across world regions. Comparative Studies 49(3).</li><li>Author, C. (2011). Education and attitudes toward government. Political Behavior 33(1).</li><li>Author, D. (2015). Income divides and satisfaction with democracy. Electoral Studies 40.</li><li>Author, E. (2013). Expert indices and citizen evaluations compared. Democratization 20(6).</li></ul></div>
</div>

<h2 class="section-title">WPSC-CPSC 2018 Presentation 1 Preview</h2>
<div class="deck">
  <div class="slide b cover"><div class="brand"><i></i>KELPO Polls</div><div class="ph" role="img" aria-label="Photo of a dense city crowd"></div><div class="band">Kindred Estimates Linking Population Outlooks Polls: An Introduction</div></div>
  <div class="slide w"><div class="t">Why merge multiple survey sources?</div><div style="display:grid;grid-template-columns:1fr 1fr;gap:3px;text-align:center"><div><span class="ico" style="display:block;margin:0 auto;width:10px;height:10px"></span>Improve democracy in developing countries to decrease inequality</div><div><span class="ico" style="display:block;margin:0 auto;width:10px;height:10px"></span>Inform healthcare policy to reduce infectious diseases</div><div><span class="ico" style="display:block;margin:0 auto;width:10px;height:10px"></span>Reduce inequality to build safer communities</div><div><span class="ico" style="display:block;margin:0 auto;width:10px;height:10px"></span>Broaden support for government and decrease conflict</div></div></div>
  <div class="slide b"><div class="t left" style="color:#fff!important">What is the vision?</div><div class="two"><div class="ph" role="img" aria-label="Photo of a researcher at a laptop" style="height:78px"></div><ol class="list"><li><span class="num">1</span>Merge all variables from all nationally representative surveys</li><li><span class="num">2</span>Undertake systematic reviews and meta-analyses to advance knowledge</li><li><span class="num">3</span>Use findings to guide policy and help the disadvantaged</li></ol></div></div>
  <div class="slide w"><div class="t">What is KELPO Polls?</div><div class="sub" style="font-weight:700">"Kindred Estimates Linking Population Outlooks Polls"</div><ul class="list"><li><span class="ico"></span>Formats and merges public opinion surveys</li><li><span class="ico"></span>Hub for quality control and coordination</li><li><span class="ico"></span>Distribution platform for merged datasets</li><li><span class="ico"></span>Source of learning materials to get involved</li><li><span class="ico"></span>Provides guidelines and instructions</li><li><span class="ico"></span>Coordinates activities to avoid duplication</li></ul></div>
  <div class="slide b"><div class="t left" style="color:#fff!important">Current Sources</div><div class="two"><ol class="list"><li><span class="num">1</span>Savanna Barometer</li><li><span class="num">2</span>Hemisphere Barometer</li><li><span class="num">3</span>Gulf Barometer</li><li><span class="num">4</span>Monsoon Barometer</li><li><span class="num">5</span>Island Election Study</li><li><span class="num">6</span>Electoral Systems Study</li></ol><div class="ph" role="img" aria-label="Portrait photo of a businessman" style="height:78px"></div></div></div>
  <div class="slide w"><div class="t">How to merge so much data?</div><ol class="list"><li><span class="num">1</span>Online crowdsourced development</li><li><span class="num">2</span>Coordinate those doing the work</li><li><span class="num">3</span>Develop shared guidelines</li><li><span class="num">4</span>Provide clear instructions</li><li><span class="num">5</span>Build upon existing frameworks</li><li><span class="num">6</span>Learn from each other and improve</li><li><span class="num">7</span>Establish online platform to organize</li><li><span class="num">8</span>Train trainers and provide courses</li></ol></div>
  <div class="slide b"><div class="t">Why should you get involved?</div><ul class="list"><li><span class="ico"></span>Division of tasks improves quality of publications</li><li><span class="ico"></span>Save time and be first to know something new</li><li><span class="ico"></span>International prestige, peer recognition and promotions</li><li><span class="ico"></span>Collaborate on systematic reviews and meta-analyses</li><li><span class="ico"></span>Learn new skills and answer new types of questions</li></ul></div>
  <div class="slide w"><div class="two"><div class="ph" role="img" aria-label="Photo of colleagues around a table" style="height:60px;margin-top:14px"></div><div><div class="t left" style="color:var(--blue)!important">How can you get involved?</div><ul class="list dots"><li>Co-author papers to help expand the resource</li><li>Download datasets for your own research</li><li>Write scripts to add sources</li><li>Become theme leader or coordinating editor</li></ul></div></div></div>

  <div class="slide b"><div class="t">What can we do with merged data?</div><div style="display:grid;grid-template-columns:1fr 1fr;gap:5px;text-align:center"><div><span class="ico" style="display:block;margin:0 auto 2px;width:12px;height:12px;border-radius:0"></span>Create public opinion indices</div><div><span class="ico" style="display:block;margin:0 auto 2px;width:12px;height:12px;border-radius:0"></span>Track trends over time</div><div><span class="ico" style="display:block;margin:0 auto 2px;width:12px;height:12px;border-radius:0"></span>Determine public opinion thresholds</div><div><span class="ico" style="display:block;margin:0 auto 2px;width:12px;height:12px;border-radius:0"></span>Larger models controlling for more factors</div></div></div>
  <div class="slide w"><div class="t">Example 1: Public Opinion Indices</div><ul class="list" style="font-size:4.4px"><li>Step 1: rename variables and reorder values</li><li>Step 2: rescale values to range from 0 to 100</li><li>Step 3: average values by country-survey</li><li>Step 4: average these scores by country-year</li></ul><div class="two"><svg viewBox="0 0 60 30" height="34"><g fill="var(--blue)"><rect x="18" y="22" width="3" height="6"/><rect x="22" y="14" width="3" height="14"/><rect x="26" y="6" width="3" height="22"/><rect x="30" y="3" width="3" height="25"/><rect x="34" y="10" width="3" height="18"/><rect x="38" y="18" width="3" height="10"/></g></svg><svg viewBox="0 0 60 30" height="34"><g fill="var(--blue)"><rect x="16" y="20" width="3" height="8"/><rect x="20" y="12" width="3" height="16"/><rect x="24" y="4" width="3" height="24"/><rect x="28" y="8" width="3" height="20"/><rect x="32" y="14" width="3" height="14"/><rect x="36" y="22" width="3" height="6"/></g></svg></div></div>
  <div class="slide w"><div class="t">Example 2: National Indices</div><div class="sub">Six-year moving averages using country-year scores</div><svg viewBox="0 0 132 50" width="132" height="56"><g fill="none" stroke-width=".8"><polyline points="4,30 14,26 24,28 34,22 40,24" stroke="var(--blue)"/><polyline points="4,20 14,24 24,20 34,26 40,22" stroke="#e05a4b"/><polyline points="48,18 58,22 68,16 78,20 84,18" stroke="var(--blue)"/><polyline points="48,28 58,26 68,30 78,24 84,26" stroke="#e05a4b"/><polyline points="92,22 102,26 112,24 122,30 128,28" stroke="var(--blue)"/><polyline points="92,30 102,22 112,28 122,20 128,24" stroke="#e05a4b"/></g></svg></div>
  <div class="slide w"><div class="t">Example 3: Demographic Trends</div><div class="sub">Satisfaction with democracy of two demographic groups</div><svg viewBox="0 0 132 50" width="132" height="56"><g fill="none" stroke-width="1"><polyline points="4,26 14,22 24,26 34,20 40,22" stroke="var(--blue)"/><polyline points="4,30 14,28 24,32 34,26 40,28" stroke="var(--blue-dark)"/><polyline points="48,20 58,18 68,22 78,16 84,18" stroke="var(--blue)"/><polyline points="48,24 58,26 68,24 78,22 84,24" stroke="var(--blue-dark)"/><polyline points="92,16 102,20 112,18 122,32 128,40" stroke="var(--blue)"/><polyline points="92,20 102,22 112,24 122,36 128,44" stroke="var(--blue-dark)"/></g></svg></div>
  <div class="slide w"><div class="t">Example 4: Effects on Social Trust</div><div class="sub">Social trust of demographic groups contrast against globalization, inequality and internet</div><svg viewBox="0 0 132 50" width="132" height="56"><g fill="none" stroke-width="1"><polyline points="4,34 40,22" stroke="var(--blue)"/><polyline points="4,28 40,26" stroke="var(--blue-dark)"/><polyline points="48,20 84,34" stroke="var(--blue)"/><polyline points="48,24 84,30" stroke="var(--blue-dark)"/><polyline points="92,34 128,20" stroke="var(--blue)"/><polyline points="92,30 128,24" stroke="var(--blue-dark)"/></g></svg></div>
  <div class="slide w"><div class="t">Example 5: Economic Indicators</div><div class="sub">Estimates of values with strongest effects on satisfaction with democracy</div><table class="tight" style="background:var(--blue);color:#fff"><tr><th></th><th>Positive</th><th>Negative</th></tr><tr><td>Government Debt (% GDP)</td><td>below 42%</td><td>above 61%</td></tr><tr><td>Real Interest Rate</td><td>below 3.8%</td><td>above 4%</td></tr><tr><td>GDP Growth</td><td>above 2%</td><td>below 0.3%</td></tr><tr><td>Income Inequality</td><td>25 to 33</td><td>above 41</td></tr><tr><td>Unemployment</td><td>below 6%</td><td>above 11%</td></tr><tr><td>Inflation</td><td>1% to 3%</td><td>above 8%</td></tr><tr><td>National Savings</td><td>above 23%</td><td>below 16%</td></tr></table></div>
  <div class="slide b"><div class="two"><div><div class="t left" style="color:#fff!important">Considerations</div><ul class="list dots"><li>Data cannot be used for commercial purposes</li><li>Users also cite the original sources</li><li>Some sources require registration, but all data is free</li></ul></div><div class="ph" role="img" aria-label="Photo of a man working at a desk" style="height:80px"></div></div></div>
  <div class="slide w"><div class="t left" style="color:var(--blue-dark)!important">Conclusion</div><ul class="list"><li><span class="ico"></span>KELPO Polls a free resource for answering new research questions</li><li><span class="ico"></span>Save time managing data and collaborate to broaden research possibilities</li><li><span class="ico"></span>Crowdsourced development aims to operate indefinitely</li><li><span class="ico"></span>Existing programs could include under-surveyed countries</li></ul></div>
</div>

<h2 class="section-title">WPSC-CPSC 2018 Presentation 2 Preview</h2>
<div class="deck">
  <div class="slide w cover" style="padding:0"><div style="position:absolute;top:4px;left:5px;font-size:4.6px;font-weight:700">Disadvantage and Democracy</div><div class="brand"><i></i>KELPO Polls</div><div class="ph" role="img" aria-label="Photo of students writing in a classroom" style="top:14px;height:46px"></div><div class="band" style="height:26px;bottom:24px;font-size:6.2px">Why Income and Education Matter for Attitudes Towards Democracy</div><div style="position:absolute;bottom:6px;left:6px;right:6px;display:flex;justify-content:space-between;font-size:4.2px;font-weight:600"><span>Dana Morrow</span><span>Owen Hartley</span></div></div>
  <div class="slide w"><div class="two"><div class="ph" role="img" aria-label="Portrait photo of a woman" style="height:70px;margin-top:10px;flex:0 0 38px"></div><div><div class="t left" style="color:var(--blue)!important">Crisis of citizen satisfaction</div><ul class="list dots"><li>Scholars note declining citizen approval (multiple studies, 2008-2016)</li><li>Attitudes towards democracy diverge in some countries</li><li>Inequality a potential causal factor</li></ul></div></div></div>
  <div class="slide b"><div class="two"><div><div class="t left" style="color:#fff!important">Capability approach</div><ul class="list dots"><li>Capability approach demonstrated shortcomings in other methods</li><li>Something on adaptive preferences</li><li>Inequality could explain differences in human welfare</li></ul></div><div class="ph" role="img" aria-label="Photo of a group of workers" style="height:40px;flex:0 0 40px"></div></div></div>
  <div class="slide w"><div class="t" style="color:var(--blue)">KELPO Polls</div><div class="bluebox" style="font-style:italic">Kindred Estimates Linking Population Outlooks Polls</div><div class="ph" role="img" aria-label="World map in light blue" style="height:50px;margin-top:4px;background:linear-gradient(135deg,#a8d1ec,#dcecf7)"></div><div class="bluebox" style="margin-top:3px;font-size:3.8px">kelpopolls.example.org/dataverse</div></div>
  <div class="slide w" style="padding-top:14px"><div class="brand" style="left:8px;right:auto"><i></i>KELPO Polls</div><div class="ph" role="img" aria-label="Photo of a crowd of people" style="height:40px"></div><div class="two" style="margin-top:3px"><ol class="list"><li><span class="num">1</span>Savanna Barometer</li><li><span class="num">2</span>Hemisphere Barometer</li><li><span class="num">3</span>Monsoon Barometer</li></ol><ol class="list"><li><span class="num">4</span>Regional Consolidation Study</li><li><span class="num">5</span>Electoral Systems Study</li></ol></div></div>
  <div class="slide w"><div class="t">Dependent Variable</div><ul class="list dots"><li>Public satisfaction with democracy</li><li>Four-point questions from respondent data</li><li>0 – 100 scale used with country-year data</li><li>Scale method: transform, double average</li></ul><svg viewBox="0 0 120 30" width="128" height="34"><g fill="var(--blue)"><rect x="36" y="24" width="3" height="5"/><rect x="40" y="18" width="3" height="11"/><rect x="44" y="10" width="3" height="19"/><rect x="48" y="4" width="3" height="25"/><rect x="52" y="2" width="3" height="27"/><rect x="56" y="6" width="3" height="23"/><rect x="60" y="12" width="3" height="17"/><rect x="64" y="18" width="3" height="11"/><rect x="68" y="23" width="3" height="6"/></g></svg></div>
  <div class="slide b" style="padding:0"><div class="t" style="padding:6px 6px 2px;text-align:left;color:#fff">Independent Variables</div><div class="ph" role="img" aria-label="Photo of a woman in a library" style="height:38px"></div><ul class="list" style="padding:4px 8px"><li><span class="ico"></span>Dummy variables representing respondent demographic groups</li><li><span class="ico"></span>Income shares of quintiles from Global Income Archive and Development Data Bank</li></ul></div>
  <div class="slide w"><div class="t">Group Differences</div><div class="two"><div class="bluebox">Satisfaction with democracy changes with income distribution</div><div class="bluebox">Satisfaction of different groups depends on relative distributions</div></div><div class="two" style="margin-top:3px;text-align:center"><div><svg viewBox="0 0 60 30" height="30"><polyline points="4,20 56,12" fill="none" stroke="var(--blue)"/><polyline points="4,16 56,14" fill="none" stroke="#9bc9e8"/></svg>Income Share of Lowest Quintile</div><div><svg viewBox="0 0 60 30" height="30"><polyline points="4,12 56,20" fill="none" stroke="var(--blue)"/><polyline points="4,14 56,16" fill="none" stroke="#9bc9e8"/></svg>Income Share of Highest Quintile</div></div></div>

  <div class="slide w"><div class="t">Diverging Trends</div><ul class="list"><li><span class="ico"></span>Democratic satisfaction of different groups diverging further apart in some countries</li><li><span class="ico"></span>Similar trends across many developed nations</li></ul><div class="two" style="text-align:center;color:var(--blue)"><div>Country A<svg viewBox="0 0 60 24" height="24"><polyline points="4,10 20,8 36,12 56,18" fill="none" stroke="var(--blue)"/><polyline points="4,14 20,14 36,16 56,20" fill="none" stroke="#9bc9e8"/></svg></div><div>Country B<svg viewBox="0 0 60 24" height="24"><polyline points="4,8 20,12 36,10 56,18" fill="none" stroke="var(--blue)"/><polyline points="4,12 20,16 36,14 56,20" fill="none" stroke="#9bc9e8"/></svg></div></div></div>
  <div class="slide b"><div class="t">Mixed-Effects</div><div class="sub">Model summary, excludes controls etc.</div><table style="background:#fff;color:#333;font-size:3.6px"><tr><th></th><th>Lowest Q.</th><th>Highest Q.</th></tr><tr><td>Lowest Quintile x Primary Edu.</td><td>0.070</td><td>0.003</td></tr><tr><td>Lowest Quintile x Tertiary Edu.</td><td>0.021</td><td>0.008</td></tr><tr><td>Lowest Quintile x Lower Inc.</td><td>0.031</td><td>0.005</td></tr><tr><td>Lowest Quintile x Higher Inc.</td><td>0.015</td><td>0.017</td></tr><tr><td>Highest Quintile x Primary Edu.</td><td>0.090</td><td>0.003</td></tr><tr><td>Highest Quintile x Tertiary Edu.</td><td>0.081</td><td>0.002</td></tr><tr><td>Highest Quintile x Lower Inc.</td><td>0.006</td><td>0.003</td></tr><tr><td>Primary Educated</td><td>0.073</td><td>0.005</td></tr><tr><td>Tertiary Educated</td><td>0.021</td><td>0.001</td></tr><tr><td>Lower Income</td><td>0.033</td><td>0.008</td></tr><tr><td>Higher Income</td><td>0.017</td><td>0.001</td></tr></table></div>
  <div class="slide w" style="padding-top:14px"><div class="brand" style="left:8px;right:auto"><i></i>KELPO Polls</div><div class="two"><div class="ph" role="img" aria-label="Photo of schoolchildren studying" style="height:68px"></div><div><div class="t left" style="color:var(--blue)!important">Implications</div><ol class="list"><li><span class="num">1</span>Important for democracies to ensure relative disadvantages are not extreme</li><li><span class="num">2</span>Some democratic measures disconnected from disadvantaged groups</li></ol></div></div></div>
  <div class="slide b" style="padding:0"><div class="t" style="padding:5px 0 2px;color:#fff">Discussion</div><div class="ph" role="img" aria-label="Photo of a classroom with many students" style="height:50px"></div><div style="text-align:center;padding:5px 8px;font-size:5px">Societies with less relative disadvantage have higher satisfaction overall</div></div>
  <div class="slide w"><div class="t left" style="color:var(--blue-dark)!important">Conclusion</div><ul class="list" style="margin-top:6px"><li><span class="ico" style="flex-basis:11px;height:11px"></span>Capability approach useful to critique inequalities beyond standard SES model</li><li><span class="ico" style="flex-basis:11px;height:11px"></span>Future research can expand areas of inequality and attitudes considered</li></ul></div>
  <div class="empty"></div><div class="empty"></div><div class="empty"></div>
</div>

<h2 class="section-title">Presentation 1 Preview</h2>
<div class="deck">
  <div class="slide b cover"><div style="position:absolute;top:4px;left:5px;font-size:4px;color:#333;z-index:2">Visualising and Comparing Global Trends</div><div class="brand"><i></i>KELPO Polls</div><div class="ph" role="img" aria-label="Photo of a crowd crossing a street" style="top:12px;height:46px"></div><div class="band" style="height:50px">Public Opinions and Perceptions (POP)<small>Dana Morrow<br>dana.morrow@example.edu</small></div></div>
  <div class="slide w"><div class="t left">Overview</div><ol class="list"><li><span class="num">1</span>Data and Variables</li><li><span class="num">2</span>Comparative National Trends</li><li><span class="num">3</span>Northland</li><li><span class="num">4</span>Westmark</li><li><span class="num">5</span>Northland vs Westmark</li></ol></div>
  <div class="slide b"><div class="t">Variable: Satisfaction with Democracy</div><div class="sub" style="font-style:italic">In general, how satisfied are you with the way democracy works in the country?</div><ul class="list"><li><span class="num">0</span>Very dissatisfied</li><li><span class="num">25</span>Dissatisfied</li><li><span class="num">50</span>Neither dissatisfied nor satisfied</li><li><span class="num">75</span>Satisfied</li><li><span class="num">100</span>Very satisfied</li></ul></div>
  <div class="slide b"><div class="t">Variable: Support for Democracy</div><div class="sub" style="font-style:italic">With which one of these statements are you most in agreement?</div><ul class="list"><li><span class="num" style="background:#fff;color:var(--blue)">0</span>In some circumstances, a non-democratic government can be preferable</li><li><span class="num" style="background:#fff;color:var(--blue)">50</span>For someone like me, the kind of regime makes no difference</li><li><span class="num" style="background:#fff;color:var(--blue)">100</span>Democracy is preferable to any other kind of government</li></ul></div>
  <div class="slide w"><div class="t" style="color:#333">Satisfaction with democracy</div><div class="sub">Northern countries</div><svg viewBox="0 0 132 70" width="132" height="74"><g fill="none" stroke-width=".7"><rect x="4" y="2" width="58" height="30" stroke="#ccc"/><rect x="70" y="2" width="58" height="30" stroke="#ccc"/><rect x="4" y="36" width="58" height="30" stroke="#ccc"/><rect x="70" y="36" width="58" height="30" stroke="#ccc"/><polyline points="8,24 20,20 32,18 44,14 58,12" stroke="var(--blue)"/><polyline points="74,20 86,22 98,16 110,18 124,12" stroke="var(--blue)"/><polyline points="8,58 20,54 32,56 44,50 58,46" stroke="var(--blue)"/><polyline points="74,54 86,50 98,52 110,46 124,44" stroke="var(--blue)"/></g></svg></div>
  <div class="slide b"><div class="t">Northland</div><div class="sub">Support for democracy by Age and Education</div><svg viewBox="0 0 132 60" width="132" height="66"><rect x="4" y="2" width="124" height="52" fill="#fff"/><g fill="none" stroke-width=".9"><polyline points="8,20 30,26 52,22 74,30 96,24 124,28" stroke="#e05a4b"/><polyline points="8,30 30,34 52,32 74,38 96,34 124,36" stroke="#e05a4b" stroke-dasharray="2 1"/><polyline points="8,16 30,18 52,14 74,20 96,16 124,18" stroke="var(--blue)"/><polyline points="8,40 30,42 52,38 74,44 96,40 124,42" stroke="var(--blue)" stroke-dasharray="2 1"/></g></svg></div>
  <div class="slide w"><div class="t" style="color:#333">Westmark</div><div class="sub">Support for Democracy by Age and Education</div><svg viewBox="0 0 132 60" width="132" height="66"><g fill="none" stroke-width=".9"><rect x="4" y="2" width="124" height="52" stroke="#ccc"/><polyline points="8,14 30,18 52,22 74,26 96,34 124,38" stroke="#e05a4b"/><polyline points="8,22 30,24 52,30 74,32 96,40 124,44" stroke="#e05a4b" stroke-dasharray="2 1"/><polyline points="8,12 30,14 52,16 74,18 96,22 124,24" stroke="var(--blue)"/><polyline points="8,26 30,28 52,30 74,34 96,36 124,38" stroke="var(--blue)" stroke-dasharray="2 1"/></g></svg></div>
  <div class="slide w"><div class="t" style="color:var(--blue)">Perceived Electoral Integrity</div><svg viewBox="0 0 132 70" width="132" height="74"><g fill="none" stroke-width=".7"><rect x="4" y="2" width="58" height="62" stroke="#ccc"/><rect x="70" y="2" width="58" height="62" stroke="#ccc"/></g><g fill="var(--blue)"><circle cx="14" cy="30" r="1.2"/><circle cx="22" cy="26" r="1.2"/><circle cx="30" cy="34" r="1.2"/><circle cx="40" cy="28" r="1.2"/><circle cx="50" cy="32" r="1.2"/></g><g fill="#e05a4b"><circle cx="80" cy="12" r="1.2"/><circle cx="90" cy="18" r="1.2"/><circle cx="100" cy="28" r="1.2"/><circle cx="110" cy="40" r="1.2"/><circle cx="120" cy="54" r="1.2"/></g><polyline points="76,10 124,58" fill="none" stroke="#e05a4b" stroke-dasharray="2 1" stroke-width=".7"/></svg></div>
</div>

<h2 class="section-title">Presentation 2 Preview</h2>
<div class="deck">
  <div class="slide b cover"><div style="position:absolute;top:4px;left:5px;font-size:4px;color:#333;z-index:2">A Global Review and Public Opinion Index</div><div class="brand"><i></i>KELPO Polls</div><div class="ph" role="img" aria-label="Photo of a hand casting a ballot" style="top:12px;height:46px"></div><div class="band" style="height:50px">Who says elections are fair?<small>Dana Morrow | dana.morrow@example.edu</small></div></div>
  <div class="slide w"><div class="t left">Overview</div><ul class="list" style="font-size:5px"><li><b>Part 1:</b>&nbsp;Introduction</li><li><b>Part 2:</b>&nbsp;Literature Review</li><li><b>Part 3:</b>&nbsp;Data and Methods</li><li><b>Part 4:</b>&nbsp;Results</li><li><b>Part 5:</b>&nbsp;Discussion</li></ul></div>
  <div class="slide b part"><div style="font-size:5px">Part 1</div><div class="lbl">INTRODUCTION</div><div class="ph" role="img" aria-label="Photo of hands typing on a laptop"></div><div style="font-size:4.8px">Perceived Electoral Integrity<br>Research Problem</div></div>
  <div class="slide w"><div class="t">Perceived Electoral Integrity</div><ul class="list"><li><span class="ico"></span>Refers to how fair or trustworthy people think elections are</li><li><span class="ico"></span>Used as dependent variable in this study</li><li><span class="ico"></span>Constructed from public survey questions about honesty, fairness, trust and freeness of elections</li><li><span class="ico"></span>Surveys use random sampling to be as nationally representative as possible</li></ul></div>
  <div class="slide b part" style="align-items:flex-start;text-align:left"><div style="font-size:5px">Part 2</div><div class="lbl">LITERATURE REVIEW</div><div class="two" style="width:100%"><div class="ph" role="img" aria-label="Photo of library bookshelves" style="height:56px;flex:0 0 56px;border:2px solid #fff"></div><ul class="list" style="font-size:4.6px"><li>• Review Criteria</li><li>• Included Studies</li><li>• Expert Indices</li><li>• Index Correlations</li><li>• Review Summary</li></ul></div></div>
  <div class="slide w" style="text-align:center"><div class="t">Review Criteria</div><div style="display:flex;justify-content:center;gap:4px;margin-bottom:3px"><span class="bluebox" style="border-radius:50%;width:18px;height:18px;line-height:12px;padding:3px 0">1994</span><span class="ico" style="width:18px;height:18px;flex:none"></span><span class="bluebox" style="border-radius:50%;width:18px;height:18px;line-height:12px;padding:3px 0">2014</span></div><div>Peer-reviewed study published between 1994 and 2014</div><div style="color:var(--blue);font-size:9px;margin:4px 0">‹ ›</div><div>Uses representative sample of general population</div></div>
  <div class="slide w"><div class="t" style="color:#333">Included Studies</div><div class="ph" role="img" aria-label="Photo of a desk with papers and glasses" style="height:36px"></div><div class="two" style="margin-top:3px;color:var(--blue);font-size:4.2px"><ul class="list dots"><li>Almeida et al. (2008)</li><li>Brandt and Keller (2014)</li><li>Costa (2007)</li><li>Dorsey et al. (2014)</li></ul><ul class="list dots"><li>Ellison (2014)</li><li>Fischer (2008)</li><li>Grant et al. (2013)</li><li>Hale and Ivers (2006)</li></ul></div></div>
  <div class="slide w"><div class="t">Index Correlations</div><div class="two"><div class="bluebox"><b>Varga (2010)</b><br>Significant positive correlation between elite scores and citizen scores</div><div class="bluebox"><b>Lindqvist et al. (2013)</b><br>Significant positive correlation between expert scores and citizen scores</div></div><ul class="list" style="margin-top:4px"><li><span class="ico"></span>Based on 32 country-year cases within the region</li><li><span class="ico"></span>Uses Parliamentary Elites of the region</li></ul></div>

  <div class="slide b part"><div style="font-size:5px">Part 3</div><div class="lbl">DATA AND METHODS</div><div class="ph" role="img" aria-label="Photo of charts on a screen" style="height:40px"></div><div style="font-size:4.6px">Survey Datasets<br>Variable Descriptions<br>Regression Models</div></div>
  <div class="slide w"><div class="t">Survey Datasets</div><div class="two" style="font-size:4.2px"><div><b>Savanna Barometer</b><br>Rounds 1–5 (1999–2015)<br><br><b>Hemisphere Barometer</b><br>2004, 2006, 2008, 2010, 2012<br><br><b>Gulf Barometer</b><br>Waves 1–3 (2006–2013)<br><br><b>Monsoon Barometer</b><br>Waves 1–3 (2001–2012)</div><div><b>Regional Social Survey</b><br>Rounds 1–6 (2002–2012)<br><br><b>Southern Barometer</b><br>1995–2013 (selected)<br><br><b>Electoral Systems Study</b><br>Modules 1–4</div></div></div>
  <div class="slide b"><div class="t">Variable Descriptions</div><table style="background:#fff;color:#333;font-size:3.8px"><tr><td style="background:var(--blue-dark);color:#fff">Perceived integrity</td><td style="text-align:left">Thinks elections generally honest</td></tr><tr><td style="background:var(--blue-dark);color:#fff">Support Winner</td><td style="text-align:left">Voted for winning party</td></tr><tr><td style="background:var(--blue-dark);color:#fff">Female Gender</td><td style="text-align:left">Respondent is female</td></tr><tr><td style="background:var(--blue-dark);color:#fff">High Income</td><td style="text-align:left">Top 20% of respondents by income</td></tr><tr><td style="background:var(--blue-dark);color:#fff">Low Income</td><td style="text-align:left">Bottom 20% of respondents by income</td></tr><tr><td style="background:var(--blue-dark);color:#fff">Tertiary Education</td><td style="text-align:left">Has some university</td></tr><tr><td style="background:var(--blue-dark);color:#fff">Primary Education</td><td style="text-align:left">Has primary or less</td></tr><tr><td style="background:var(--blue-dark);color:#fff">Age</td><td style="text-align:left">Age grouped 18–29 to 65+</td></tr></table></div>
  <div class="slide w"><div class="t">Global Index Correlations 1</div><div class="sub">Significant (p-value &lt;0.0001) correlations with Perceived Electoral Integrity</div><ul class="list" style="background:#eaf4fb;padding:3px"><li>.39 All Respondents (n = 379)</li><li>.39 Tertiary Educated (n = 378)</li><li>.29 Primary Educated (n = 377)</li><li>.46 Higher Income (n = 378)</li><li>.31 Lower Income (n = 378)</li><li>.35 Election Winner (n = 235)</li><li>.50 Election Loser (n = 242)</li></ul></div>
  <div class="slide b part"><div style="font-size:5px">Part 5</div><div class="lbl">DISCUSSIONS</div><div class="ph" role="img" aria-label="Photo of a conference room" style="height:40px"></div><div class="two" style="font-size:4.2px;width:100%"><div>Age in Region<br>Gender in Region<br>Education in Region</div><div>Income in Region<br>Public Opinion Index<br>Conclusion</div></div></div>
  <div class="slide w"><div class="t">Age in Region</div><div class="two"><div class="ph" role="img" aria-label="Photo of an elderly man" style="height:50px;flex:0 0 40px"></div><div style="font-size:4.4px">Prior studies found older people to have positive perceptions of electoral integrity<br><br>For regional countries, this remains true, but more frequent finding is that younger people have negative perceptions</div></div><div style="text-align:center;margin-top:3px;font-size:4.4px">Moreover, it is not just older people, but specifically elderly or retired people (65+) who have the most positive views</div></div>
  <div class="slide w"><div class="t">Gender in Region</div><div class="two"><div style="font-size:4.4px">Regional countries differ from other regions of the world in that females tend to have more positive perceptions of electoral integrity<br><br>Three countries each have multiple positive relationships for different survey rounds</div><div class="ph" role="img" aria-label="Photo of a smiling woman" style="height:66px;flex:0 0 42px"></div></div></div>
  <div class="slide w"><div class="t left">Conclusion</div><ul class="list"><li><span class="ico"></span>Cross-national and cross-regional approach provides insights not available when studying single countries</li><li><span class="ico"></span>Public opinion index will be a useful measure to complement existing expert opinion indices</li><li><span class="ico"></span>Comments and critiques more than welcome</li></ul></div>
</div>

</div>
</body>
</html>
```